Web site design for Brivolt Software (www.brivoltsoftware-example.com)

Need the design as well as the html for the website. The brief is given in the attached file.
If possible, would like to use pencil sketches instead of images to give a unique look to the site.
Target Market(s)
small Software product companies
Industry/Entity Type
Software
Coding
Coded - Design and coding required
Number of Pages Required
5+ page

```html
<!DOCTYPE html>
<html lang="en">
<head>
<meta charset="utf-8">
<title>Brivolt Software</title>
<link href="https://fonts.googleapis.com/css2?family=Bebas+Neue&family=Open+Sans:ital,wght@0,400;0,600;0,700;1,400&display=swap" rel="stylesheet">
<style>
:root{
  --red:#e30b13;
  --ink:#1f1f1f;
  --text:#6b6b6b;
  --muted:#9a9a9a;
  --white:#ffffff;
  --panel:#f2f1ef;
  --panel-2:#f6f6f6;
  --line:#e4e4e4;
  --yellow:#e6df9c;
}
*{box-sizing:border-box;margin:0;padding:0}
html,body{width:1200px;height:4918px;overflow:hidden}
body{font-family:"Open Sans",Arial,sans-serif;color:var(--text);background:var(--white);position:relative}
.section{position:absolute;left:0;width:1200px;overflow:hidden}
.abs{position:absolute}
.display{font-family:"Bebas Neue",Impact,sans-serif;color:var(--ink);line-height:.98;letter-spacing:.5px}
.display .accent{color:var(--red)}
.body-copy{font-size:12px;line-height:1.6;color:var(--text)}
.btn{position:absolute;display:flex;align-items:center;justify-content:center;font-family:"Bebas Neue",Impact,sans-serif;font-size:14px;letter-spacing:1px;color:var(--white)}
.btn-red{background:var(--red)}
.btn-outline{border:2px solid var(--white)}

/* Hero */
.hero{top:0;height:672px;background:linear-gradient(180deg,#2d2e31 0%,#4b4c50 45%,#3a2c26 78%,#2b1f1b 100%)}
.hero-photo{position:absolute;inset:0;background:radial-gradient(ellipse at 70% 45%,rgba(190,190,195,.35),rgba(0,0,0,0) 60%)}
.hero-shade{position:absolute;inset:0;background:linear-gradient(90deg,rgba(0,0,0,.45),rgba(0,0,0,.05))}
.brand{left:148px;top:62px;font-family:"Bebas Neue",Impact,sans-serif;font-size:34px;color:var(--white);letter-spacing:2px;display:flex;align-items:center;gap:10px}
.brand-mark{width:14px;height:14px;background:var(--white)}
.nav{left:551px;top:68px;display:flex;gap:34px;font-family:"Bebas Neue",Impact,sans-serif;font-size:16px;letter-spacing:1px;color:var(--white)}
.nav .active{border-bottom:2px solid var(--white);padding-bottom:6px}
.hero-title{left:157px;top:218px;font-size:60px;color:var(--white)}
.hero-lead{left:157px;top:382px;width:560px;font-size:17px;font-style:italic;color:var(--white);line-height:1.5}

/* About */
.about{top:672px;height:581px;background:var(--white)}
.about-photo{left:420px;top:0;width:295px;height:581px;background:linear-gradient(160deg,#f01818 0%,#c80a0a 45%,#8f0606 100%)}
.about-title{left:157px;top:70px;font-size:62px}
.about-text{left:157px;top:270px;width:256px}
.hours{position:absolute;left:420px;width:295px;text-align:right;padding-right:55px;color:var(--white)}
.hours h4{font-family:"Bebas Neue",Impact,sans-serif;font-weight:400;font-size:24px;line-height:1;letter-spacing:.5px}
.hours span{font-family:"Bebas Neue",Impact,sans-serif;font-size:13px;letter-spacing:1px}
.hours-dot{position:absolute;left:690px;width:50px;height:50px;border-radius:50%;background:var(--white);border:3px solid var(--red);display:flex;align-items:center;justify-content:center}
.hours-text{position:absolute;left:764px;width:273px}

/* Services */
.services{top:1253px;height:600px;background:var(--panel)}
.services-title{left:157px;top:354px;font-size:62px}
.card{position:absolute;width:193px;background:var(--white);box-shadow:0 2px 8px rgba(0,0,0,.06);text-align:center;padding-top:28px}
.card h5{font-family:"Bebas Neue",Impact,sans-serif;font-weight:400;font-size:15px;color:var(--red);letter-spacing:.5px;margin-top:12px}
.card p{font-size:10px;line-height:1.55;padding:4px 26px 0}

/* Blog */
.blog{top:1853px;height:574px;background:var(--white)}
.blog-title{left:157px;top:338px;font-size:62px}
.thumb{position:absolute;left:420px;width:193px;height:131px}
.date{position:absolute;left:0;top:24px;width:42px;height:46px;background:var(--red);color:var(--white);text-align:center;font-family:"Bebas Neue",Impact,sans-serif;line-height:1}
.date b{display:block;font-weight:400;font-size:26px;padding-top:4px}
.date small{font-size:11px;letter-spacing:1px}
.post{position:absolute;left:633px;width:194px}
.post h6{font-family:"Bebas Neue",Impact,sans-serif;font-weight:400;font-size:15px;color:var(--ink);letter-spacing:.5px;margin-bottom:4px}
.post p{font-size:10px;line-height:1.5}
.feature{left:846px;top:63px;width:191px;height:446px;background:linear-gradient(180deg,#8a8680 0%,#5c5651 55%,#3e3935 100%)}
.feature-caption{position:absolute;left:20px;bottom:18px;right:14px;color:var(--white)}
.feature-caption h6{font-family:"Bebas Neue",Impact,sans-serif;font-weight:400;font-size:16px;line-height:1.05}
.feature-caption p{font-size:10px;line-height:1.5;margin-top:6px}

/* Team */
.team{top:2427px;height:597px;background:var(--panel-2)}
.team-title{left:157px;top:361px;font-size:62px}
.member{position:absolute;top:59px;width:193px;text-align:center}
.portrait{width:193px;height:309px}
.member h5{font-family:"Bebas Neue",Impact,sans-serif;font-weight:400;font-size:26px;color:var(--ink);margin-top:30px;line-height:1}
.member .role{font-family:"Bebas Neue",Impact,sans-serif;font-size:13px;color:var(--red);letter-spacing:.5px}
.member p{font-size:10px;line-height:1.55;padding:6px 16px 0}

/* Portfolio */
.portfolio{top:3024px;height:597px;background:var(--white)}
.tile{position:absolute}
.portfolio-title{left:279px;top:370px;font-size:52px;line-height:1.02}
.portfolio-title .light{color:var(--ink);font-family:"Bebas Neue",Impact,sans-serif}

/* Packages */
.packages{top:3621px;height:594px;background:var(--panel-2)}
.packages-title{left:157px;top:352px;font-size:62px}
.plan{position:absolute;top:59px;width:193px;height:472px;background:var(--white);box-shadow:0 2px 8px rgba(0,0,0,.06);text-align:center;padding-top:34px}
.plan h5{font-family:"Bebas Neue",Impact,sans-serif;font-weight:400;font-size:26px;color:var(--ink);margin-top:22px;line-height:1}
.plan .role{font-family:"Bebas Neue",Impact,sans-serif;font-size:13px;color:var(--red);letter-spacing:.5px}
.plan p{font-size:10px;line-height:1.55;padding:14px 20px 0}
.plan .price{font-family:"Bebas Neue",Impact,sans-serif;font-size:46px;color:var(--ink);margin-top:24px;line-height:1}
.plan .btn{left:37px;bottom:32px;width:119px;height:36px;font-size:13px}

/* Contact */
.contact{top:4215px;height:597px;background:var(--white)}
.contact-title{left:157px;top:66px;font-size:58px}
.contact-photo{left:508px;top:0;width:692px;height:597px;background:linear-gradient(135deg,#2a2522 0%,#5a463a 40%,#8b7060 62%,#3b3330 100%)}
.contact-item{position:absolute;left:157px;display:flex;gap:20px}
.contact-item svg{flex:none}
.contact-item h6{font-family:"Bebas Neue",Impact,sans-serif;font-weight:400;font-size:17px;color:var(--red);letter-spacing:.5px;line-height:1.1}
.contact-item p{font-size:10px;line-height:1.5;width:200px}

/* Footer */
.footer{top:4812px;height:106px;background:var(--panel-2);display:flex;align-items:center;justify-content:center;font-size:10px;color:var(--muted)}
</style>
</head>
<body>

<header class="section hero">
  <div class="hero-photo" role="img" aria-label="Photograph of a bright open office interior with desks and chairs"></div>
  <div class="hero-shade"></div>
  <div class="abs brand"><span class="brand-mark"></span>BRIVOLT</div>
  <nav class="abs nav">
    <span class="active">HOME</span><span>ABOUT US</span><span>SERVICES</span><span>PORTFOLIO</span><span>OUR TEAM</span><span>NEWS</span><span>CONTACT</span>
  </nav>
  <h1 class="abs display hero-title">WELCOME TO THE <span class="accent">BRIVOLT</span><br><span class="accent">SOFTWARE</span> COMPANY</h1>
  <p class="abs hero-lead">Lorem ipsum dolor sit amet, consectetur adipiscing elit, sed do eiusmod tempor incididunt ut labore et dolore magna aliqua. Ut</p>
  <a class="btn btn-red" style="left:157px;top:489px;width:105px;height:36px">READ MORE</a>
  <a class="btn btn-outline" style="left:315px;top:489px;width:135px;height:36px">READ MORE</a>
</header>

<section class="section about">
  <h2 class="abs display about-title">ABOUT<br><span class="accent">BRIVOLT</span><br>SOFTWARE</h2>
  <p class="abs body-copy about-text">Lorem ipsum dolor sit amet, consectetur adipiscing elit, sed do eiusmod tempor incididunt ut labore et dolore magna aliqua. Ut enim ad minim veniam, quis nostrud exercitation ullamco laboris nisi ut aliquip ex ea commodo consequat. Lorem ipsum dolor sit amet, consectetur adipiscing elit, sed do eiusmod tempor incididunt ut labore et dolore magna aliqua ut enim ad minim veniam.</p>
  <div class="abs about-photo" role="img" aria-label="Red-toned abstract photograph of folded paper shapes"></div>

  <div class="hours" style="top:48px"><h4>WORKING HOURS</h4><span>DESIGNER NAME</span></div>
  <div class="hours-dot" style="top:44px"><svg width="22" height="22" viewBox="0 0 24 24" fill="none" stroke="#e30b13" stroke-width="2"><circle cx="12" cy="12" r="9"/><path d="M12 7v5l3 2"/></svg></div>
  <p class="hours-text body-copy" style="top:28px;font-size:10px">Lorem ipsum dolor sit amet, consectetur adipiscing elit, sed do eiusmod tempor incididunt ut labore et dolore magna aliqua. Ut enim ad minim veniam, quis nostrud exercitation.</p>

  <div class="hours" style="top:173px"><h4>WORKING HOURS</h4><span>DESIGNER NAME</span></div>
  <div class="hours-dot" style="top:169px"><svg width="22" height="22" viewBox="0 0 24 24" fill="none" stroke="#e30b13" stroke-width="2"><circle cx="12" cy="12" r="9"/><path d="M12 7v5l3 2"/></svg></div>
  <p class="hours-text body-copy" style="top:153px;font-size:10px">Lorem ipsum dolor sit amet, consectetur adipiscing elit, sed do eiusmod tempor incididunt ut labore et dolore magna aliqua. Ut enim ad minim veniam, quis nostrud exercitation.</p>

  <div class="hours" style="top:294px"><h4>WORKING HOURS</h4><span>DESIGNER NAME</span></div>
  <div class="hours-dot" style="top:290px"><svg width="22" height="22" viewBox="0 0 24 24" fill="none" stroke="#e30b13" stroke-width="2"><circle cx="12" cy="12" r="9"/><path d="M12 7v5l3 2"/></svg></div>
  <p class="hours-text body-copy" style="top:274px;font-size:10px">Lorem ipsum dolor sit amet, consectetur adipiscing elit, sed do eiusmod tempor incididunt ut labore et dolore magna aliqua. Ut enim ad minim veniam, quis nostrud exercitation.</p>

  <div class="hours" style="top:428px"><h4>WORKING HOURS</h4><span>DESIGNER NAME</span></div>
  <div class="hours-dot" style="top:424px"><svg width="22" height="22" viewBox="0 0 24 24" fill="none" stroke="#e30b13" stroke-width="2"><circle cx="12" cy="12" r="9"/><path d="M12 7v5l3 2"/></svg></div>
  <p class="hours-text body-copy" style="top:408px;font-size:10px">Lorem ipsum dolor sit amet, consectetur adipiscing elit, sed do eiusmod tempor incididunt ut labore et dolore magna aliqua. Ut enim ad minim veniam, quis nostrud exercitation.</p>
</section>

<section class="section services">
  <h2 class="abs display services-title">OUR<br><span class="accent">SPECIAL</span><br>SERVICES</h2>

  <div class="card" style="left:420px;top:65px;height:224px">
    <svg width="40" height="40" viewBox="0 0 24 24" fill="none" stroke="#333" stroke-width="1.3"><circle cx="12" cy="12" r="9"/><ellipse cx="12" cy="12" rx="4" ry="9"/><path d="M3 12h18M5 7h14M5 17h14"/></svg>
    <h5>ACHIEVES</h5>
    <p>Lorem ipsum dolor sit amet, consectetur adipiscing elit, sed do eiusmod tempor incididunt ut</p>
  </div>
  <div class="card" style="left:633px;top:65px;height:224px">
    <svg width="40" height="40" viewBox="0 0 24 24" fill="none" stroke="#333" stroke-width="1.3"><path d="M7 17a4 4 0 0 1-.5-8 5.5 5.5 0 0 1 10.7 1.2A3.5 3.5 0 0 1 17 17"/><path d="M12 11v9M9 17l3 3 3-3"/></svg>
    <h5>DESIGNER</h5>
    <p>Lorem ipsum dolor sit amet, consectetur adipiscing elit, sed do eiusmod tempor incididunt ut</p>
  </div>
  <div class="card" style="left:846px;top:65px;height:224px">
    <svg width="40" height="40" viewBox="0 0 24 24" fill="none" stroke="#333" stroke-width="1.3"><rect x="5" y="7" width="14" height="13"/><path d="M5 7l2-3h10l2 3M10 11h4"/></svg>
    <h5>PERFECT DESIGN</h5>
    <p>Lorem ipsum dolor sit amet, consectetur adipiscing elit, sed do eiusmod tempor incididunt ut</p>
  </div>
  <div class="card" style="left:420px;top:308px;height:223px">
    <svg width="40" height="40" viewBox="0 0 24 24" fill="none" stroke="#333" stroke-width="1.3"><path d="M3 12a9 8 0 0 1 18 0z"/><path d="M12 12v7a2 2 0 0 1-4 0"/></svg>
    <h5>PERFECT DESIGN</h5>
    <p>Lorem ipsum dolor sit amet, consectetur adipiscing elit, sed do eiusmod tempor incididunt ut</p>
  </div>
  <div class="card" style="left:633px;top:308px;height:223px">
    <svg width="40" height="40" viewBox="0 0 24 24" fill="none" stroke="#333" stroke-width="1.3"><path d="M14 5H5v15h15v-9"/><path d="M18 3l3 3-9 9H9v-3z"/></svg>
    <h5>ACHIEVES</h5>
    <p>Lorem ipsum dolor sit amet, consectetur adipiscing elit, sed do eiusmod tempor incididunt ut</p>
  </div>
  <div class="card" style="left:846px;top:308px;height:223px">
    <svg width="40" height="40" viewBox="0 0 24 24" fill="none" stroke="#333" stroke-width="1.3"><path d="M10 13V4a1.5 1.5 0 0 1 3 0v7l5 1.5a2 2 0 0 1 1.4 2.3L18.5 20H10l-3.5-5a1.5 1.5 0 0 1 2.3-1.9z"/></svg>
    <h5>ACHIEVES</h5>
    <p>Lorem ipsum dolor sit amet, consectetur adipiscing elit, sed do eiusmod tempor incididunt ut</p>
  </div>
</section>

<section class="section blog">
  <h2 class="abs display blog-title">LATEST<br><span class="accent">DESIGN</span><br>BLOG</h2>

  <div class="thumb" style="top:63px;background:linear-gradient(135deg,#d9d4cc,#a89e92)" role="img" aria-label="Photograph of a desk with stationery"><div class="date"><b>24</b><small>MAY</small></div></div>
  <div class="post" style="top:63px"><h6>DESIGNED AND BUILT WITH CARE</h6><p>Lorem ipsum dolor sit amet, consectetur adipiscing elit, sed do eiusmod tempor incididunt ut labore et dolore magna aliqua. Ut enim ad minim veniam quis.</p></div>

  <div class="thumb" style="top:217px;background:linear-gradient(135deg,#e9ecef,#9aa6b2)" role="img" aria-label="Photograph of a young man in a cap"><div class="date"><b>24</b><small>MAY</small></div></div>
  <div class="post" style="top:217px"><h6>DESIGNED AND BUILT WITH CARE</h6><p>Lorem ipsum dolor sit amet, consectetur adipiscing elit, sed do eiusmod tempor incididunt ut labore et dolore magna aliqua. Ut enim ad minim veniam quis.</p></div>

  <div class="thumb" style="top:374px;background:linear-gradient(135deg,#3a3230,#8c3a2e 60%,#2a2424)" role="img" aria-label="Photograph of a dim shop interior with shelves"><div class="date"><b>24</b><small>MAY</small></div></div>
  <div class="post" style="top:374px"><h6>DESIGNED AND BUILT WITH CARE</h6><p>Lorem ipsum dolor sit amet, consectetur adipiscing elit, sed do eiusmod tempor incididunt ut labore et dolore magna aliqua. Ut enim ad minim veniam quis.</p></div>

  <div class="abs feature" role="img" aria-label="Photograph of a street musician playing guitar">
    <div class="date"><b>24</b><small>MAY</small></div>
    <div class="feature-caption"><h6>DESIGNED AND BUILT WITH CARE</h6><p>Lorem ipsum dolor sit amet, consectetur adipiscing elit, sed do eiusmod.</p></div>
  </div>
</section>

<section class="section team">
  <h2 class="abs display team-title">CREATIVE<br><span class="accent">TEAM</span><br>MEMBERS</h2>
  <div class="member" style="left:420px">
    <div class="portrait" style="background:linear-gradient(160deg,#d8cdc4,#a88f80 55%,#6d5a4f)" role="img" aria-label="Close-up portrait photograph of a team member with glasses"></div>
    <h5>DESIGNER NAME</h5><div class="role">GRAPHIC DESIGNER</div>
    <p>Lorem ipsum dolor sit amet, consectetur adipiscing elit, sed do eiusmod tempor incididunt ut labore et dolore magna.</p>
  </div>
  <div class="member" style="left:633px">
    <div class="portrait" style="background:linear-gradient(160deg,#e2d6cc,#b49481 55%,#7a5e4e)" role="img" aria-label="Close-up portrait photograph of a bearded team member"></div>
    <h5>DESIGNER NAME</h5><div class="role">GRAPHIC DESIGNER</div>
    <p>Lorem ipsum dolor sit amet, consectetur adipiscing elit, sed do eiusmod tempor incididunt ut labore et dolore magna.</p>
  </div>
  <div class="member" style="left:846px">
    <div class="portrait" style="background:linear-gradient(160deg,#f1e6dc,#d2b29c 55%,#a57d66)" role="img" aria-label="Close-up portrait photograph of a smiling team member"></div>
    <h5>DESIGNER NAME</h5><div class="role">GRAPHIC DESIGNER</div>
    <p>Lorem ipsum dolor sit amet, consectetur adipiscing elit, sed do eiusmod tempor incididunt ut labore et dolore magna.</p>
  </div>
</section>

<section class="section portfolio">
  <div class="tile" style="left:0;top:0;width:600px;height:200px;background:linear-gradient(135deg,#d8d2c6,#b9b0a2)" role="img" aria-label="Photograph of business card mockups on paper"></div>
  <div class="tile" style="left:600px;top:0;width:600px;height:200px;background:linear-gradient(135deg,#e6df9c,#d6cf8a)" role="img" aria-label="Photograph of a newspaper mockup on a yellow background"></div>
  <div class="tile" style="left:0;top:200px;width:240px;height:397px;background:linear-gradient(180deg,#f4f4f4,#e2e2e2)" role="img" aria-label="Photograph of a beer glass and bottle mockup"></div>
  <h2 class="abs display portfolio-title">OUR<br><span class="accent">PORTFOLIO</span><br>GALLERY</h2>
  <div class="tile" style="left:600px;top:200px;width:240px;height:397px;background:linear-gradient(180deg,#ece5a8,var(--yellow))" role="img" aria-label="Photograph of a paper tube and coffee cup mockup"></div>
  <div class="tile" style="left:840px;top:200px;width:360px;height:397px;background:linear-gradient(180deg,#e9e9e7,#d9d6d0)" role="img" aria-label="Photograph of a kraft paper bag mockup"></div>
</section>

<section class="section packages">
  <h2 class="abs display packages-title">OUR<br><span class="accent">DESIGINS</span><br>PACKAGE</h2>
  <div class="plan" style="left:420px">
    <svg width="40" height="40" viewBox="0 0 24 24" fill="none" stroke="#333" stroke-width="1.3"><path d="M9 18h6M10 21h4M12 3a6 6 0 0 0-3.5 10.9V16h7v-2.1A6 6 0 0 0 12 3z"/></svg>
    <h5>DESIGNER NAME</h5><div class="role">GRAPHIC DESIGNER</div>
    <p>Lorem ipsum dolor sit amet, consectetur adipiscing elit, sed do eiusmod tempor incididunt ut labore et dolore magna aliqua. Ut enim ad minim veniam, quis nostrud exercitation.</p>
    <div class="price">$50</div>
    <a class="btn btn-red">READ MORE</a>
  </div>
  <div class="plan" style="left:633px">
    <svg width="40" height="40" viewBox="0 0 24 24" fill="none" stroke="#333" stroke-width="1.3"><path d="M2 4h3l2.5 11h11L21 7H6.5"/><circle cx="9" cy="19" r="1.5"/><circle cx="17" cy="19" r="1.5"/></svg>
    <h5>DESIGNER NAME</h5><div class="role">GRAPHIC DESIGNER</div>
    <p>Lorem ipsum dolor sit amet, consectetur adipiscing elit, sed do eiusmod tempor incididunt ut labore et dolore magna aliqua. Ut enim ad minim veniam, quis nostrud exercitation.</p>
    <div class="price">$500</div>
    <a class="btn btn-red">READ MORE</a>
  </div>
  <div class="plan" style="left:846px">
    <svg width="40" height="40" viewBox="0 0 24 24" fill="none" stroke="#333" stroke-width="1.3"><rect x="6" y="3" width="15" height="13"/><path d="M3 7v14h14"/><path d="M6 14l4-4 3 3 2-2 6 5"/><circle cx="16" cy="7" r="1.3"/></svg>
    <h5>DESIGNER NAME</h5><div class="role">GRAPHIC DESIGNER</div>
    <p>Lorem ipsum dolor sit amet, consectetur adipiscing elit, sed do eiusmod tempor incididunt ut labore et dolore magna aliqua. Ut enim ad minim veniam, quis nostrud exercitation.</p>
    <div class="price">$1000</div>
    <a class="btn btn-red">READ MORE</a>
  </div>
</section>

<section class="section contact">
  <h2 class="abs display contact-title">HOW<br><span class="accent">FIND US</span></h2>
  <div class="contact-item" style="top:213px">
    <svg width="40" height="40" viewBox="0 0 24 24" fill="none" stroke="#444" stroke-width="1.3"><path d="M12 21s-6-6.5-6-11a6 6 0 0 1 12 0c0 4.5-6 11-6 11z"/><circle cx="12" cy="10" r="2.2"/></svg>
    <div><h6>ADRESS</h6><p>Lorem ipsum dolor sit amet, consectetur adipiscing elit, sed do eiusmod tempor.</p></div>
  </div>
  <div class="contact-item" style="top:312px">
    <svg width="40" height="40" viewBox="0 0 24 24" fill="none" stroke="#444" stroke-width="1.3"><path d="M5 3h4l2 5-2.5 1.5a11 11 0 0 0 6 6L16 13l5 2v4a2 2 0 0 1-2 2A16 16 0 0 1 3 5a2 2 0 0 1 2-2z"/></svg>
    <div><h6>CALL US</h6><p>+000 555 0100<br>+000 555 0101</p></div>
  </div>
  <div class="contact-item" style="top:411px">
    <svg width="40" height="40" viewBox="0 0 24 24" fill="none" stroke="#444" stroke-width="1.3"><rect x="3" y="6" width="18" height="13"/><path d="M3 6l9 7 9-7"/></svg>
    <div><h6>EMAIL</h6><p>info@brivoltsoftware-example.com</p></div>
  </div>
  <div class="contact-item" style="top:509px">
    <svg width="40" height="40" viewBox="0 0 24 24" fill="none" stroke="#444" stroke-width="1.3"><rect x="3" y="4" width="18" height="12"/><path d="M9 20h6M12 16v4"/></svg>
    <div><h6>WEBSITE</h6><p>www.brivoltsoftware-example.com</p></div>
  </div>
  <div class="abs contact-photo" role="img" aria-label="Photograph of a laptop on a wooden desk with a white chair"></div>
</section>

<footer class="section footer">Copyright © 2017. All Rights Reserved.</footer>

</body>
</html>
```